Lantern Lane Town Footpath Chronicle Trek

We are launching a different kind of city historical walking tour company with a slightly darker approach using historical but real stories that have long been forgotten from living memory.
Our tour is going to contain a lot of very thoroughly researched stories ranging from 50 to 150 years past that takes the customer into the actual-real life past of the city streets.  Stories that may contains some dark undertones and stories with a twist or that seem eccentric to us now but were entirely normal back in olden times - minus the dry historical facts that most tours engage in..
Our tours are going to run both day and night and will incorporate real history / real Lantern Lane, so some of the stories will be quite serious (e.g.- there are actual murders from 100 years ago, baffling court cases, even a bit of poetry written by murderers, suicides, love triangles, you name it.  We are aiming for a mystery/history theme and are aiming to attract tourists who are interested in getting a different kind of history.

We're not going for scares and even though we expect people to enjoy our tours;  we're not aiming at light fun and frivolity.  I guess if you wanted to give us a tv rating we'd be aiming at M to MA15+.
If I was to give you another analogy using the literature world.  Think Edwin Harrowgates Nocturno rather than the Moonrise Saga of movies.  Or Clara Wendham's Gravemoor rather than the Pickwells.  Even Crown of Embers rather than a soap opera.
Our stories are being carefully crafted and are packed with unexpected twists, turns & revelations whilst remaining all 100% true.  We have approx 15-20 stories for each tour and we're designing them in a way that each story will trigger a different range of emotions in the listeners on a regular basis.  We're being very careful to keep it fresh for each story so that it will next to impossible for our guests to zone out!  I personally can't stand going on a tour where mildly interesting facts are read out.  We like deep, rich stories rather than pop entertainment.
We want the website to generate a feeling/atmosphere for our product that draws the right crowd to our tours as well as making it easy to make a booking.  Basic features to include:-
Home Page
Bookings Page
Integration with a booking system will be required here via use of plugin code.
Private Functions Page
We are hoping to integrate with a booking system via use of plugin code.  If not, then a simple form enquiry type input e.g.- name, emails, subject, contact, details, preferred date/time, etc).
About Us Page :-
Dark; a euphemism for the unknown or the forgotten.  Think dark ages, dark matter, dark energy; things where knowledge is uncertain or unknown are often termed dark.   Lantern lane brings back the hidden past, the forgotten past, the past that may not want to be remembered……but these are real stories....real stories that come from the streets around you.

Some of these stories may be tales of dark things.....some may simply be a charming reminder of days gone by…..regardless these stories are compelling reminders of the amazing times that precede us…..and the forgotten people of yesteryear finally get a chance to have their story told to a fresh audience.  Through you, the people of yesterday get to live again.  Will you like what you hear?

Contact Us page:-
•	A form input type page.
•	Include space for our phone number
•	Include space for our email address
Other Items:-
Social Media Links; we will be looking for social media icons to link to our social media pages to Chatterbook, Snapfolio, Chirplet.
Subscription; we want to also capture an input email address box for site visitors.  We will be launching a weekly Lantern Lane podcast / email newsetter; with a weekly Lantern Lane from a different place in the world and we want some way for people to subscribe.

Updates
Project Deadline Extended
Reason: A few additional photos have been uploaded.  Feel free to utilize if helpful.  Our stories range from the 1800s to 1950s in an era with beautiful old Victorian buildings.  I'm putting through the extension just to give some more time to see if this gives any more ideas and inspiration.  Thank you for all the great submissions.

Target Market(s)
Tourists that want to hear a darker version of the city they are visiting. Stories that other tour companies would not even think of covering. The real history of the events that ordinary people lived through that didn't necessarily make the history books. All stories are true; as per project description.
Industry/Entity Type
Tourism
Coding
Coded - Design and coding required
Number of Pages Required
5+ page
Colors
Designer to choose colors to be used in the design.
Look and feel

```html
<!DOCTYPE html>
<html lang="en">
<head>
<meta charset="utf-8">
<title>Lantern Lane – City History Tours</title>
<link rel="stylesheet" href="https://fonts.googleapis.com/css2?family=Oswald:wght@400;500;600&family=Rajdhani:wght@600;700&family=Lato:wght@400;700&display=swap">
<style>
:root{
  --bg:#1b1b1b;
  --bg-deep:#121212;
  --panel:#2e2e2e;
  --red:#e3262c;
  --white:#ffffff;
  --text:#d6d6d6;
  --excerpt:#c4c4c4;
  --muted:#9a9a9a;
}
*{margin:0;padding:0;box-sizing:border-box}
html,body{width:1200px;height:3666px;overflow:hidden;background:var(--bg-deep)}
body{font-family:"Lato",sans-serif;color:var(--text)}
.canvas{position:relative;width:1200px;height:3666px;overflow:hidden;
  background:
    radial-gradient(ellipse 700px 500px at 85% 62%,rgba(70,70,70,.35),transparent 70%),
    radial-gradient(ellipse 600px 400px at 10% 80%,rgba(60,60,60,.3),transparent 70%),
    linear-gradient(180deg,#1e1e1e 0%,#1a1a1a 40%,#232323 70%,#1a1a1a 100%)}
.abs{position:absolute}
.heading{font-family:"Rajdhani",sans-serif;font-weight:700;color:var(--red);font-size:26px;letter-spacing:1px;text-align:center;width:100%;left:0}
.btn-outline{position:absolute;border:1.5px solid #bdbdbd;border-radius:5px;color:var(--white);font-size:14px;display:flex;align-items:center;justify-content:center}

/* header / hero */
.hero{left:0;top:0;width:1200px;height:770px;
  background:
    radial-gradient(ellipse 520px 160px at 30% 150px,rgba(120,120,120,.55),transparent 70%),
    radial-gradient(ellipse 420px 130px at 78% 190px,rgba(105,105,105,.5),transparent 70%),
    radial-gradient(ellipse 500px 200px at 22% 560px,rgba(95,95,95,.45),transparent 70%),
    radial-gradient(ellipse 520px 220px at 82% 560px,rgba(85,85,85,.45),transparent 70%),
    radial-gradient(ellipse 380px 160px at 52% 640px,rgba(70,70,70,.5),transparent 70%),
    linear-gradient(180deg,#3c3c3c 0%,#545454 14%,#3e3e3e 26%,#2b2b2b 36%,#353535 55%,#2c2c2c 72%,#1d1d1d 100%)}
.brand{left:112px;top:92px;font-family:"Oswald",sans-serif;font-weight:500;font-size:30px;color:var(--red);letter-spacing:1px;display:flex;align-items:center;gap:10px}
.brand-dot{width:16px;height:16px;background:var(--red);border-radius:50%}
.nav{right:100px;top:80px;display:flex;gap:36px;font-family:"Oswald",sans-serif;font-size:14px;color:var(--white);letter-spacing:1px;align-items:center}
.hero-title{left:0;width:1200px;top:425px;text-align:center;font-family:"Oswald",sans-serif;font-weight:500;font-size:48px;color:var(--white);letter-spacing:1px}

/* booking */
.field{position:absolute;height:42px;background:var(--panel);color:#e0e0e0;font-size:12px;padding:0 18px;display:flex;align-items:center}
.field.select{justify-content:space-between}
.send{position:absolute;background:var(--red);color:var(--white);font-size:12px;display:flex;align-items:center;justify-content:center}

.about-text{left:190px;width:820px;top:1042px;text-align:center;font-size:13.5px;line-height:17px;color:#e2e2e2}

/* stories */
.tabs{left:240px;top:1245px;display:flex}
.tab{font-size:14px;color:var(--white);letter-spacing:1px;width:127px;height:28px;display:flex;align-items:center;justify-content:center;border-radius:5px}
.tab.active{border:1.5px solid #cfcfcf;width:100px;margin-right:27px}
.story-photo{left:147px;top:1295px;width:905px;height:465px;
  background:
    radial-gradient(ellipse 200px 150px at 42% 58%,rgba(120,120,120,.45),transparent 70%),
    radial-gradient(ellipse 160px 220px at 70% 40%,rgba(130,130,130,.4),transparent 70%),
    radial-gradient(ellipse 150px 200px at 15% 40%,rgba(90,90,90,.45),transparent 70%),
    radial-gradient(ellipse 260px 110px at 45% 85%,rgba(20,20,20,.6),transparent 70%),
    linear-gradient(180deg,#2a2a2a 0%,#3b3b3b 35%,#333 60%,#1f1f1f 100%)}
.book-photo{left:152px;top:1880px;width:922px;height:565px;border-radius:10px;
  background:
    radial-gradient(ellipse 90px 260px at 50% 38%,rgba(25,25,25,.85),transparent 70%),
    radial-gradient(ellipse 260px 300px at 27% 40%,rgba(150,150,150,.45),transparent 70%),
    radial-gradient(ellipse 260px 300px at 73% 40%,rgba(150,150,150,.45),transparent 70%),
    radial-gradient(ellipse 420px 120px at 50% 92%,rgba(10,10,10,.6),transparent 70%),
    linear-gradient(180deg,#3a3a3a 0%,#4a4a4a 30%,#333 70%,#1e1e1e 100%)}
.slide-copy{left:235px;top:2218px;width:320px}
.slide-copy .kicker{font-family:"Rajdhani",sans-serif;font-weight:700;color:var(--red);font-size:25px;letter-spacing:1px}
.slide-copy .meta{font-size:15px;color:#e0e0e0;margin-top:2px}
.slide-copy .title{font-family:"Rajdhani",sans-serif;font-weight:700;color:var(--white);font-size:23px;letter-spacing:1.5px;margin-top:10px}
.slide-copy p{font-size:13px;line-height:16px;color:#c8c8c8;margin-top:4px}
.slide-copy .more{font-size:13px;color:#e0e0e0}

/* blog */
.blog-sub{left:0;width:1200px;top:2598px;text-align:center;font-size:13.5px;color:#e2e2e2}
.card{position:absolute;top:2644px;width:300px}
.card-photo{width:300px;height:192px;position:relative}
.photo-alley{background:radial-gradient(ellipse 50px 140px at 50% 45%,#7a7a7a,transparent 80%),linear-gradient(90deg,#1a1a1a,#3a3a3a 45%,#2a2a2a 70%,#151515)}
.photo-skyline{background:radial-gradient(ellipse 220px 60px at 50% 70%,rgba(120,120,120,.5),transparent 70%),linear-gradient(180deg,#5a5a5a 0%,#444 35%,#2a2a2a 60%,#1a1a1a 100%)}
.photo-figure{background:radial-gradient(ellipse 110px 120px at 55% 55%,#6a6a6a,transparent 75%),linear-gradient(120deg,#2a2a2a,#4a4a4a 60%,#8a8a8a)}
.date{position:absolute;left:0;top:10px;width:36px;height:36px;background:var(--red);color:var(--white);text-align:center;font-size:14px;font-weight:700;line-height:16px;padding-top:3px}
.date small{display:block;font-size:9px;font-weight:400;line-height:10px}
.card h3{font-weight:400;font-size:14px;color:#e6e6e6;margin-top:16px;letter-spacing:.5px}
.card .info{display:flex;justify-content:space-between;font-size:12px;color:var(--muted);margin-top:7px;align-items:center}
.card .info span{display:flex;align-items:center;gap:6px}
.card p{font-size:13px;line-height:16px;color:var(--excerpt);margin-top:18px;font-weight:400}
.card .more,.footer-about .more{font-size:13px;color:#d0d0d0;margin-top:6px;display:flex;align-items:center;gap:6px}

/* subscribe */
.sub-title{top:3137px}
.sub-line{left:0;width:1200px;top:3170px;text-align:center;font-family:"Rajdhani",sans-serif;font-weight:600;font-size:16px;color:#dcdcdc;letter-spacing:1.5px}
.sub-input{left:298px;top:3216px;width:570px;height:38px;background:#303030;font-size:11px;color:#a0a0a0;letter-spacing:2px;padding-left:18px;display:flex;align-items:center}
.sub-btn{left:758px;top:3220px;width:103px;height:30px;background:var(--red);color:var(--white);font-family:"Rajdhani",sans-serif;font-weight:700;font-size:14px;letter-spacing:1px;display:flex;align-items:center;justify-content:center}

/* footer */
.footer-logo{left:127px;top:3336px;display:flex;align-items:center;gap:12px}
.footer-logo .circle{width:74px;height:74px;border-radius:50%;background:var(--red)}
.footer-logo .name{font-weight:700;color:var(--white);font-size:16px}
.footer-about{left:130px;top:3450px;width:250px;font-size:13.5px;line-height:16px;color:var(--white);font-weight:700}
.col-title{font-weight:700;font-size:14px;color:var(--white);letter-spacing:.5px}
.col-title::after{content:"";display:block;width:56px;height:2px;background:#cfcfcf;margin-top:10px}
.links{list-style:none;margin-top:22px}
.links li{font-size:13.5px;color:var(--white);line-height:26px;display:flex;align-items:center;gap:18px}
.contact{list-style:none;margin-top:22px}
.contact li{font-size:12.5px;color:var(--white);line-height:15px;display:flex;gap:12px;margin-bottom:13px}
.contact svg{flex:none;margin-top:1px}
.gallery{display:grid;grid-template-columns:repeat(3,70px);gap:3px;margin-top:22px}
.gallery div{height:100px;background:linear-gradient(180deg,#5a5a5a,#2a2a2a)}
.bottom-bar{left:0;top:3612px;width:1200px;height:54px;background:#060606;display:flex;align-items:center;justify-content:space-between;padding:0 120px 0 130px}
.legal{font-size:13.5px;color:var(--white);font-weight:700}
.socials{display:flex;gap:8px}
.socials span{width:22px;height:22px;border-radius:50%;background:#f2f2f2}
</style>
</head>
<body>
<div class="canvas">

  <div class="abs hero" role="img" aria-label="Dusky black and white aerial view of old city rooftops under a cloudy sky"></div>
  <div class="abs brand"><span class="brand-dot"></span>LANTERN LANE</div>
  <nav class="abs nav">
    <span>HOME</span><span>ABOUT</span><span>PAST STORIES</span><span>TOURS</span><span>BLOG</span><span>CONTACT</span>
    <svg width="14" height="12" viewBox="0 0 14 12"><rect y="0" width="14" height="2" fill="#fff"/><rect y="5" width="14" height="2" fill="#fff"/><rect y="10" width="14" height="2" fill="#fff"/></svg>
  </nav>
  <h1 class="abs hero-title">TRAVEL WITH LANTERN LANE</h1>

  <h2 class="abs heading" style="top:788px;font-size:22px">BOOKING</h2>
  <div class="field" style="left:117px;top:833px;width:310px">Name</div>
  <div class="field" style="left:445px;top:833px;width:310px">Email</div>
  <div class="field" style="left:777px;top:833px;width:311px">Phone</div>
  <div class="field select" style="left:117px;top:899px;width:255px">Where <svg width="9" height="6"><path d="M0 0h9L4.5 6z" fill="#aaa"/></svg></div>
  <div class="field select" style="left:389px;top:899px;width:256px">When <svg width="9" height="6"><path d="M0 0h9L4.5 6z" fill="#aaa"/></svg></div>
  <div class="field select" style="left:662px;top:899px;width:255px">Guests <svg width="9" height="6"><path d="M0 0h9L4.5 6z" fill="#aaa"/></svg></div>
  <div class="send" style="left:934px;top:899px;width:154px;height:44px">Send</div>

  <h2 class="abs heading" style="top:1000px">ABOUT US</h2>
  <p class="abs about-text">Dark; a euphemism for the unknown or the forgotten. Think dark ages,dark matter, dark energy; things where knowledge is uncertain or unknown are often termed dark.Lantern lane brings back the hidden past, the forgotten past, the past that may not want to be remembered.....but these are real stories...real stories that come from the streets around you.</p>
  <div class="btn-outline" style="left:543px;top:1112px;width:119px;height:32px">Read More</div>

  <h2 class="abs heading" style="top:1186px">PAST STORIES</h2>
  <svg class="abs" style="left:540px;top:1228px" width="120" height="4"><rect width="120" height="1.5" y="1" fill="#bdbdbd"/></svg>
  <div class="abs tabs">
    <div class="tab active">STORIES 1</div>
    <div class="tab">STORIES 2</div>
    <div class="tab">STORIES 3</div>
    <div class="tab">STORIES 1</div>
    <div class="tab">STORIES 1</div>
    <div class="tab">STORIES 1</div>
  </div>
  <div class="abs story-photo" role="img" aria-label="Shadowy Victorian hall with a long candlelit banquet table"></div>
  <div class="btn-outline" style="left:525px;top:1777px;width:140px;height:32px">View More</div>

  <div class="abs book-photo" role="img" aria-label="Open old book with a dark iron railway corridor rising from its pages"></div>
  <svg class="abs" style="left:76px;top:2160px" width="22" height="32" viewBox="0 0 22 32"><path d="M18 2L4 16l14 14" fill="none" stroke="#e8e8e8" stroke-width="4"/></svg>
  <svg class="abs" style="left:1112px;top:2160px" width="22" height="32" viewBox="0 0 22 32"><path d="M4 2l14 14L4 30" fill="none" stroke="#e8e8e8" stroke-width="4"/></svg>
  <div class="abs slide-copy">
    <div class="kicker">REAL STORIES</div>
    <div class="meta">8 day 2 Weak</div>
    <div class="title">EXPERIENCES TOURS</div>
    <p>Lorem Ipsum is simply dummy text of the printing and typesetting industry.</p>
    <div class="more">Read More.....</div>
  </div>

  <h2 class="abs heading" style="top:2558px">OUR BLOG</h2>
  <p class="abs blog-sub">Lorem Ipsum is simply dummy text of the printing and typesetting industry.</p>

  <article class="card" style="left:139px">
    <div class="card-photo photo-alley" role="img" aria-label="Narrow dim alley between old brick buildings"><div class="date">10<small>Nov</small></div></div>
    <h3>DARK CITY</h3>
    <div class="info"><span><svg width="11" height="11" viewBox="0 0 12 12"><circle cx="6" cy="6" r="5" fill="none" stroke="#9a9a9a" stroke-width="1.4"/><path d="M6 3v3h2.5" fill="none" stroke="#9a9a9a" stroke-width="1.4"/></svg>November 02, 2017</span><span><svg width="12" height="11" viewBox="0 0 12 11"><path d="M6 10L1.5 5.5A2.6 2.6 0 016 2a2.6 2.6 0 014.5 3.5z" fill="none" stroke="#ccc" stroke-width="1.3"/></svg>12</span></div>
    <p>Lorem Ipsum is simply dummy text of the printing and typesetting industry. Lorem dummy text ever since the 1500s.</p>
    <div class="more">Read More <svg width="12" height="12" viewBox="0 0 12 12"><circle cx="6" cy="6" r="5.5" fill="#d0d0d0"/><path d="M5 3.5L7.5 6 5 8.5" fill="none" stroke="#222" stroke-width="1.4"/></svg></div>
  </article>

  <article class="card" style="left:464px">
    <div class="card-photo photo-skyline" role="img" aria-label="City skyline at dusk under a stormy sky"><div class="date">11<small>Oct</small></div></div>
    <h3>REAL STORIES</h3>
    <div class="info"><span><svg width="11" height="11" viewBox="0 0 12 12"><circle cx="6" cy="6" r="5" fill="none" stroke="#9a9a9a" stroke-width="1.4"/><path d="M6 3v3h2.5" fill="none" stroke="#9a9a9a" stroke-width="1.4"/></svg>November 02, 2017</span><span><svg width="12" height="11" viewBox="0 0 12 11"><path d="M6 10L1.5 5.5A2.6 2.6 0 016 2a2.6 2.6 0 014.5 3.5z" fill="none" stroke="#ccc" stroke-width="1.3"/></svg>12</span></div>
    <p>Lorem Ipsum is simply dummy text of the printing and typesetting industry. Lorem dummy text ever since the 1500s.</p>
    <div class="more">Read More <svg width="12" height="12" viewBox="0 0 12 12"><circle cx="6" cy="6" r="5.5" fill="#d0d0d0"/><path d="M5 3.5L7.5 6 5 8.5" fill="none" stroke="#222" stroke-width="1.4"/></svg></div>
  </article>

  <article class="card" style="left:787px">
    <div class="card-photo photo-figure" role="img" aria-label="Grainy monochrome scene of a distressed figure in shadow"><div class="date">25<small>Oct</small></div></div>
    <h3>DARK CITY STORIES</h3>
    <div class="info"><span><svg width="11" height="11" viewBox="0 0 12 12"><circle cx="6" cy="6" r="5" fill="none" stroke="#9a9a9a" stroke-width="1.4"/><path d="M6 3v3h2.5" fill="none" stroke="#9a9a9a" stroke-width="1.4"/></svg>November 02, 2017</span><span><svg width="12" height="11" viewBox="0 0 12 11"><path d="M6 10L1.5 5.5A2.6 2.6 0 016 2a2.6 2.6 0 014.5 3.5z" fill="none" stroke="#ccc" stroke-width="1.3"/></svg>12</span></div>
    <p>Lorem Ipsum is simply dummy text of the printing and typesetting industry. Lorem dummy text ever since the 1500s.</p>
    <div class="more">Read More <svg width="12" height="12" viewBox="0 0 12 12"><circle cx="6" cy="6" r="5.5" fill="#d0d0d0"/><path d="M5 3.5L7.5 6 5 8.5" fill="none" stroke="#222" stroke-width="1.4"/></svg></div>
  </article>

  <div class="btn-outline" style="left:537px;top:3011px;width:128px;height:32px">View More</div>

  <h2 class="abs heading sub-title">SUBSCRIBE TO OUR NEWS LETTER</h2>
  <p class="abs sub-line">TO RECEIVE THE LATEST NEWS &amp; UPDATE</p>
  <div class="abs sub-input">YOUR EMAIL</div>
  <div class="abs sub-btn">SUBMIT</div>

  <div class="abs footer-logo"><span class="circle"></span><span class="name">Lantern Lane</span></div>
  <div class="abs footer-about">
    Lorem Ipsum is simply dummy text of the printing and types etting ind Lorem Ipsu in been the industry's ....
    <div class="more">Read More.. <svg width="14" height="14" viewBox="0 0 12 12"><circle cx="6" cy="6" r="5" fill="none" stroke="#ddd" stroke-width="1.2"/><path d="M5 3.5L7.5 6 5 8.5" fill="none" stroke="#ddd" stroke-width="1.2"/></svg></div>
  </div>

  <div class="abs" style="left:430px;top:3345px">
    <div class="col-title">QUICK LINKS</div>
    <ul class="links">
      <li><svg width="6" height="9"><path d="M0 0l6 4.5L0 9z" fill="#fff"/></svg>Home</li>
      <li><svg width="6" height="9"><path d="M0 0l6 4.5L0 9z" fill="#fff"/></svg>About</li>
      <li><svg width="6" height="9"><path d="M0 0l6 4.5L0 9z" fill="#fff"/></svg>Tours</li>
      <li><svg width="6" height="9"><path d="M0 0l6 4.5L0 9z" fill="#fff"/></svg>Blog</li>
      <li><svg width="6" height="9"><path d="M0 0l6 4.5L0 9z" fill="#fff"/></svg>Booking</li>
    </ul>
  </div>

  <div class="abs" style="left:660px;top:3345px">
    <div class="col-title">ADDRESS</div>
    <ul class="contact">
      <li><svg width="11" height="14" viewBox="0 0 11 14"><path d="M5.5 13S1 8 1 5a4.5 4.5 0 019 0c0 3-4.5 8-4.5 8z" fill="none" stroke="#fff" stroke-width="1.3"/><circle cx="5.5" cy="5" r="1.5" fill="#fff"/></svg><span>123 East Lantern Row,<br>Suite 123, USA</span></li>
      <li><svg width="12" height="12" viewBox="0 0 12 12"><path d="M2 1h2.5l1 3-1.5 1a7 7 0 003 3l1-1.5 3 1V11A1 1 0 0110 12 10 10 0 010 2a1 1 0 011-1z" fill="#fff"/></svg><span>+00 123 456 7890</span></li>
      <li><svg width="13" height="10" viewBox="0 0 13 10"><rect x=".6" y=".6" width="11.8" height="8.8" fill="none" stroke="#fff" stroke-width="1.2"/><path d="M.6.6l5.9 5 5.9-5" fill="none" stroke="#fff" stroke-width="1.2"/></svg><span>info@lanternlane.com</span></li>
      <li><svg width="12" height="12" viewBox="0 0 12 12"><circle cx="6" cy="6" r="5" fill="none" stroke="#fff" stroke-width="1.3"/><path d="M6 3v3h2.5" fill="none" stroke="#fff" stroke-width="1.3"/></svg><span>Mon-Sat 9:00am-6:00pm</span></li>
    </ul>
  </div>

  <div class="abs" style="left:865px;top:3345px">
    <div class="col-title">GALLERY</div>
    <div class="gallery">
      <div role="img" aria-label="Night street scene"></div>
      <div role="img" aria-label="Old city rooftops"></div>
      <div role="img" aria-label="Misty skyline"></div>
    </div>
  </div>

  <div class="abs bottom-bar">
    <span class="legal">Privacy policy - Legal mentions - Terms and Conditions</span>
    <div class="socials" aria-label="Social links: Chatterbook, Snapfolio, Chirplet">
      <span></span><span></span><span></span><span></span><span></span><span></span>
    </div>
  </div>

</div>
</body>
</html>
```